Northgate Roofing Works Inc Business cards

Commercial and Residential Roofing contractor needs design logo and card design. Can be single or double sided but must incorporate:
Persons Name:
Persons Title:
Mailing Address: PO Box 3719
Physical Address: 58 Fenwick Lane
Oakridge, Ma. 01642
800-316-5842
508-712-5842
Fax: 508-712-5867
Cell: Person Cell number
email address
Website: WWW.northgateroofworks.com

Target Market(s)

Residential home owners and commercial building owners

Industry/Entity Type

Roofing

Contact Information for Business Card

Persons Name:
Persons Title:
Oakridge, Ma. 01642
800-316-5842
508-712-5842
Fax: 508-712-5867
Cell: Person Cell number
email address

Logo Text

Large enough to service small enough to care

Font styles to use
Serif

Colors
0355a3

Requirements
Must have
• Commercial and Residential Roofing contractor needs design logo and card design. Can be single or double sided but must incorporate:
• Persons Name:
• Persons Title:
• Mailing Address: PO Box 3719
• Physical Address: 58 Fenwick Lane
• Oakridge, Ma. 01642
• 800-316-5842
• 508-712-5842
• Fax: 508-712-5867
• Cell: Person Cell number
• email address
• Website: WWW.northgateroofworks.com
Nice to have
• ..
Should not have
• I'm looking for something different. I have had the same card for 23 years. I attached what both sides of my present card looks like.

```html
<!DOCTYPE html>
<html lang="en">
<head>
<meta charset="utf-8">
<title>Northgate Roofing Works Inc — Business Cards</title>
<link rel="stylesheet" href="https://fonts.googleapis.com/css2?family=Questrial&family=Tinos&display=swap">
<style>
  :root {
    --brand-blue: #0355a3;
    --paper: #ffffff;
    --stage: #eceef0;
    --ink-grey: #6b6b6b;
    --accent-grey: #a9abae;
  }
  * { box-sizing: border-box; margin: 0; padding: 0; }
  html, body { width: 1200px; height: 840px; overflow: hidden; }
  body {
    background: var(--stage);
    font-family: "Questrial", "Century Gothic", sans-serif;
    display: flex;
    align-items: center;
    justify-content: center;
    gap: 40px;
  }
  .card {
    position: relative;
    width: 540px;
    height: 309px;
    box-shadow: 0 6px 18px rgba(0,0,0,0.12);
    overflow: hidden;
  }

  /* Front */
  .card--front {
    background: var(--brand-blue);
    display: flex;
    align-items: center;
    justify-content: center;
  }
  .wordmark {
    display: flex;
    align-items: center;
    gap: 14px;
  }
  .wordmark__square {
    width: 44px;
    height: 44px;
    background: var(--paper);
  }
  .wordmark__name {
    color: var(--paper);
    font-size: 30px;
    letter-spacing: 0.5px;
  }

  /* Back */
  .card--back { background: var(--paper); }
  .card--back .wordmark {
    position: absolute;
    left: 30px;
    top: 74px;
    gap: 8px;
  }
  .card--back .wordmark__square {
    width: 20px;
    height: 20px;
    background: var(--brand-blue);
  }
  .card--back .wordmark__name {
    color: var(--brand-blue);
    font-size: 16px;
    letter-spacing: 0.2px;
  }
  .person {
    position: absolute;
    right: 34px;
    top: 30px;
  }
  .person__name {
    font-family: "Tinos", "Times New Roman", serif;
    color: var(--brand-blue);
    font-size: 27px;
    font-weight: 400;
  }
  .person__title {
    color: var(--ink-grey);
    font-size: 14px;
    margin-top: 2px;
    padding-left: 74px;
  }
  .contact {
    position: absolute;
    font-size: 11px;
    line-height: 17px;
    color: var(--ink-grey);
    display: grid;
    grid-template-columns: auto auto;
    column-gap: 6px;
  }
  .contact dt {
    color: var(--brand-blue);
    font-weight: 700;
    font-family: Verdana, "Questrial", sans-serif;
    font-size: 10.5px;
    text-align: right;
  }
  .contact dd { white-space: nowrap; }
  .contact--address { left: 30px; top: 150px; }
  .contact--address .contact__continue { grid-column: 2; }
  .contact--direct { left: 312px; top: 122px; }

  .edge-band {
    position: absolute;
    left: 0;
    bottom: 0;
    width: 540px;
    height: 70px;
  }
  .edge-band__blue { fill: var(--brand-blue); }
  .edge-band__grey { fill: var(--accent-grey); }
</style>
</head>
<body>

  <section class="card card--front" aria-label="Card front">
    <div class="wordmark">
      <span class="wordmark__square"></span>
      <span class="wordmark__name">northgate roofing works</span>
    </div>
  </section>

  <section class="card card--back" aria-label="Card back">
    <div class="wordmark">
      <span class="wordmark__square"></span>
      <span class="wordmark__name">northgate roofing works</span>
    </div>

    <div class="person">
      <h1 class="person__name">Dale Kowalczyk</h1>
      <p class="person__title">President</p>
    </div>

    <dl class="contact contact--address">
      <dt>Mailing Address:</dt><dd>PO Box 3719</dd>
      <dt>Physical Address:</dt><dd>58 Fenwick Lane</dd>
      <dd class="contact__continue">Oakridge, Ma. 01642</dd>
      <dd class="contact__continue">800-316-5842</dd>
      <dd class="contact__continue">508-712-5842</dd>
    </dl>

    <dl class="contact contact--direct">
      <dt>Fax:</dt><dd>508-712-5867</dd>
      <dt>Cell:</dt><dd>508-419-2736</dd>
      <dt>Email:</dt><dd>dale@northgateroofworks.com</dd>
      <dt>Website:</dt><dd>www.northgateroofworks.com</dd>
    </dl>

    <svg class="edge-band" viewBox="0 0 540 70" aria-hidden="true">
      <polygon class="edge-band__blue" points="0,56 392,56 430,4 430,70 0,70"/>
      <polygon class="edge-band__grey" points="442,0 450,0 450,56 540,56 540,70 442,70"/>
    </svg>
  </section>

</body>
</html>
```